Craft Flavoured Beer Family Extension Desing

We are a Canadian craft brewery looking for the design of a new line of beer we wish to launch within an existing family of products. Our beers are high craft beers that retail for a significant price. Example, 4.49$ for 500 mL vs. 1.49$ for a 500 mL Valdermost.

The line of beer that is being designed here is for a craft flavoured beer line targeted to women. This will be light tasting beers with light fruit flavors targeted to consumers who like beer but are not ready for the strong IPA which are generally found in the craft beer offerings.

The Marisette line, which is the name of this new product, is a ''cousin'' of the existing Gaston-Ferrand Line (more info below).

Target Market(s)

60% Females 40% Males - 21 to 40 years old

Industry/Entity Type

Brewery

Requirements
Must have
• The products will be an INDIRECT family/line extension of the Gaston-Ferrand line of products (design attached). There needs to be some similarities, but it cannot be too close. There are 3 main features on the Gaston-Ferrand label (attached) : (1) the font used for the Logo; (2) the shape of the label; (3) the motif printed on the label.
• The shape of the label must be different than the current shape.
• However, the font of the logo (Gaston-Ferrand) can be the same and the motif printed on the label can be used. Using one of these elements is sufficient to link this new brand with the Gaston-Ferrand brand.
• The name of the product will be MARISETTE
Nice to have
• The bottle, the size, the ABV will be different than for the Gaston-Ferrand beers.
• There will be 3 flavours initially : Blueberry, Grapefruit and Raspberry.
• There needs to be a back label, but if you design, you can use the exact same information as there is currently.
Should not have
• We don't want any fruit pictures or designs on the labels.

```html
<!DOCTYPE html>
<html lang="en">
<head>
<meta charset="UTF-8">
<title>Marisette – Craft Beer Labels</title>
<link href="https://fonts.googleapis.com/css2?family=Anton&family=Cinzel:wght@400;600&family=Roboto+Condensed:wght@500;700&display=swap" rel="stylesheet">
<style>
  :root {
    --amber: #7b3a12;
    --amber-light: #9a4c1a;
    --ink: #fbf6ee;
    --raspberry: #9c2f6e;
    --grapefruit: #ee7b2d;
    --blackberry: #574f8c;
  }
  * { margin: 0; padding: 0; box-sizing: border-box; }
  html, body { width: 1200px; height: 1000px; overflow: hidden; }
  body {
    background: radial-gradient(ellipse at 50% 55%, var(--amber-light), var(--amber) 70%);
    color: var(--ink);
    position: relative;
  }
  .label {
    position: absolute;
    top: 500px;
    width: 260px;
    display: flex;
    flex-direction: column;
    align-items: center;
    text-align: center;
  }
  .label--raspberry { left: 178px; }
  .label--grapefruit { left: 470px; }
  .label--blackberry { left: 758px; }
  .crest-motif {
    width: 200px;
    height: 112px;
    border-radius: 100px 100px 4px 4px;
    background: linear-gradient(180deg, rgba(251,246,238,0.28), rgba(251,246,238,0.12));
  }
  .brewery-name {
    margin-top: 6px;
    font-family: "Cinzel", serif;
    font-weight: 600;
    font-size: 11px;
    letter-spacing: 2px;
    white-space: nowrap;
  }
  .product-name {
    margin-top: 6px;
    font-family: "Anton", sans-serif;
    font-weight: 400;
    font-size: 50px;
    line-height: 1.05;
    letter-spacing: 1px;
    white-space: nowrap;
  }
  .flavour-band {
    margin-top: 8px;
    width: 228px;
    padding: 5px 0 4px;
    font-family: "Roboto Condensed", sans-serif;
    font-weight: 700;
    font-size: 17px;
    letter-spacing: 0.3px;
    text-transform: uppercase;
    white-space: nowrap;
  }
  .label--raspberry .flavour-band { background: var(--raspberry); }
  .label--grapefruit .flavour-band { background: var(--grapefruit); }
  .label--blackberry .flavour-band { background: var(--blackberry); }
  .origin {
    margin-top: 6px;
    display: flex;
    align-items: center;
    gap: 8px;
    font-family: "Cinzel", serif;
    font-size: 10px;
    letter-spacing: 2px;
    white-space: nowrap;
  }
  .origin-dot {
    width: 5px; height: 5px; border-radius: 50%;
    background: var(--ink);
  }
  .specs {
    margin-top: 6px;
    display: flex;
    align-items: center;
    font-family: "Roboto Condensed", sans-serif;
    font-weight: 500;
    font-size: 14px;
    white-space: nowrap;
  }
  .specs-divider {
    width: 1px; height: 16px;
    background: var(--ink);
    margin: 0 12px;
  }
  .footer-motif {
    margin-top: 8px;
    width: 90px;
    height: 50px;
    border-radius: 4px 4px 45px 45px;
    background: linear-gradient(180deg, rgba(251,246,238,0.24), rgba(251,246,238,0.08));
  }
</style>
</head>
<body>
  <section class="label label--raspberry">
    <div class="crest-motif" role="img" aria-label="Ornate white filigree crest motif"></div>
    <p class="brewery-name">BRASSERIE LES DEUX RIVES</p>
    <h2 class="product-name">MARISETTE</h2>
    <p class="flavour-band">Raspberry Craft Beer</p>
    <p class="origin"><span class="origin-dot"></span>BRASSÉE AU QUÉBEC<span class="origin-dot"></span></p>
    <p class="specs"><span>500 ML</span><span class="specs-divider"></span><span>ALC. 5% VOL</span></p>
    <div class="footer-motif" role="img" aria-label="Small filigree ornament"></div>
  </section>

  <section class="label label--grapefruit">
    <div class="crest-motif" role="img" aria-label="Ornate white filigree crest motif"></div>
    <p class="brewery-name">BRASSERIE LES DEUX RIVES</p>
    <h2 class="product-name">MARISETTE</h2>
    <p class="flavour-band">Grapefruit Craft Beer</p>
    <p class="origin"><span class="origin-dot"></span>BRASSÉE AU QUÉBEC<span class="origin-dot"></span></p>
    <p class="specs"><span>500 ML</span><span class="specs-divider"></span><span>ALC. 5% VOL</span></p>
    <div class="footer-motif" role="img" aria-label="Small filigree ornament"></div>
  </section>

  <section class="label label--blackberry">
    <div class="crest-motif" role="img" aria-label="Ornate white filigree crest motif"></div>
    <p class="brewery-name">BRASSERIE LES DEUX RIVES</p>
    <h2 class="product-name">MARISETTE</h2>
    <p class="flavour-band">Blackberry Craft Beer</p>
    <p class="origin"><span class="origin-dot"></span>BRASSÉE AU QUÉBEC<span class="origin-dot"></span></p>
    <p class="specs"><span>500 ML</span><span class="specs-divider"></span><span>ALC. 5% VOL</span></p>
    <div class="footer-motif" role="img" aria-label="Small filigree ornament"></div>
  </section>
</body>
</html>
```